| 希望する色 | オレンジ系 追記事項: 白×オレンジ系 |
| サイズ | A4 |
| ページ数 | 両面 |
▽ターゲット
【 地域住民 】向けの【 案内 】用に新しいチラシデザインを作成したいと考えており、デザイナー・クリエイターの方向けにコンペを開催いたします。 ▽サイズ 【A4縦置き両面カラー】×【コート紙90kg】 ▽参考デザイン サイト名:【 ことりデンタルクリニック 】 ▽参考URL:【 http://www.kotori-dc.example/ 】 過去のチラシ、及び、素材を添付致しました。(6/4虫歯予防デー、8/20ハチマルニイマル運動、11/8いい歯の日) 今回のチラシは6月4日のくるみ健口デーに向けたコンペになります。 集合写真は最新メンバーのものが「素材」にあります。 写真は適宜加工して頂いて構いません。 前回コンペで採用させて頂いたものが最新です。 裏面の日本とスウェーデンとの比較は、デザインを変えて同内容でお願いします。 【痛くなってから治してもらっていませんか?】に変わるキャッチコピーをお願いします。 【治療ではなく予防のために】【痛くない時こそ定期的に】【予防こそが医療費削減】…何か上手いものをお願いします。 医療広告ガイドラインというものが御座いますので、念のためご留意願います。 過去のチラシでは「粗品進呈券」を付けたらグレーでしたが、それ以外は大丈夫です。 よろしくお願い申し上げます。 |
今回採用させて頂いた理由は、スタッフ&数名の患者様にアンケートをとった結果になります。
特に、当院外観に用いているウェーブ状ウィンドサインのデザインを取り入れてくれたことに感動しました。
皆様ご提案を頂きありがとうございました。どれも本当に素敵なものばかりでした。
・8/20(ナナサンゴロク運動)
・11/8(あおばの日)
こちらのコンペも開催する予定ですので、今後ともよろしくお願い申し上げます。

```html
<!DOCTYPE html>
<html lang="ja">
<head>
<meta charset="utf-8">
<title>くるみ健口デー 定期検診のご案内</title>
<link href="https://fonts.googleapis.com/css2?family=Noto+Sans+JP:wght@400;500;700;900&family=M+PLUS+Rounded+1c:wght@500;800&display=swap" rel="stylesheet">
<style>
:root{
  --orange:#ef7f1a;
  --orange-deep:#d9650a;
  --orange-pale:#fdebd6;
  --ink:#3a3a3a;
  --sub:#666;
  --paper:#ffffff;
  --photo-grey:#d9d6d2;
  --photo-warm:#e8dccd;
  --sweden-blue:#2a62b0;
  --sweden-yellow:#f6c800;
  --japan-red:#d21f2b;
}
*{box-sizing:border-box;margin:0;padding:0}
html,body{width:848px;height:1200px;overflow:hidden;background:var(--paper)}
body{font-family:"Noto Sans JP",sans-serif;color:var(--ink);position:relative}
.abs{position:absolute}
.photo{background:linear-gradient(135deg,var(--photo-warm),var(--photo-grey))}

/* header */
.hero-photo{left:0;top:0;width:848px;height:260px;background:linear-gradient(120deg,#f2efec 0%,#dcd5cf 55%,#c9bfb6 100%)}
.day-tag{left:18px;top:14px;padding:8px 26px;background:var(--orange);color:#fff;border-radius:24px;font-weight:700;font-size:24px;letter-spacing:1px}
.wave{left:0;top:220px;width:848px;height:70px}

.headline-rule{left:40px;width:768px;height:3px;background:var(--orange)}
.headline{left:0;top:306px;width:848px;line-height:60px;text-align:center;font-family:"M PLUS Rounded 1c",sans-serif;font-weight:800;font-size:52px;color:var(--orange);letter-spacing:3px}

/* left story */
.story-title{left:40px;top:392px;font-size:26px;font-weight:900;line-height:1.35}
.story-body{left:40px;top:478px;width:370px;font-size:12.5px;line-height:1.75;color:var(--sub)}
.story-lead{left:40px;top:628px;width:380px;font-size:16px;font-weight:700;color:var(--orange-deep);white-space:nowrap}

/* right compare */
.guide-tag{left:652px;top:380px;padding:3px 12px;border:2px solid var(--orange);color:var(--orange);font-weight:700;font-size:16px;background:#fff}
.compare{left:430px;top:428px;width:390px;height:134px;border:2px solid var(--orange);border-radius:8px;background:var(--orange-pale)}
.compare-title{left:20px;top:-15px;padding:2px 14px;background:var(--orange);color:#fff;font-weight:900;font-size:17px;border-radius:14px}
.stat{font-weight:900;color:var(--ink);font-size:13px;line-height:1}
.stat small{font-size:11px;font-weight:500;color:var(--sub);display:block;margin-bottom:3px}
.stat b{font-size:28px;color:var(--orange-deep)}
.stat.sw b{color:var(--sweden-blue)}
.country{font-size:11px;font-weight:700;text-align:center}

.doctor-info{left:430px;top:576px;width:228px;font-size:11px;line-height:1.55;color:var(--sub)}
.doctor-info .name{font-size:15px;font-weight:700;color:var(--ink)}
.doctor-photo{left:668px;top:566px;width:180px;height:100px;background:linear-gradient(160deg,#f4ede6,#dcccbd)}

/* features */
.features-band{left:0;top:672px;width:848px;height:260px;background:#fafafa;border-top:4px solid var(--orange)}
.feat-title{font-size:15px;font-weight:700;color:var(--orange-deep);border-bottom:2px solid var(--orange);padding-bottom:2px;margin-bottom:4px;white-space:nowrap}
.feat-text{font-size:10.5px;line-height:1.6;color:var(--sub)}

/* footer */
.clinic-name{left:40px;top:948px;display:flex;align-items:center;gap:10px;font-size:24px;font-weight:700;color:var(--orange-deep)}
.clinic-dot{width:24px;height:24px;border-radius:50%;background:var(--orange)}
.clinic-en{left:76px;top:984px;font-size:13px;color:var(--sub)}
.hours{left:40px;top:1010px;border-collapse:collapse;font-size:13px}
.hours th{background:var(--orange);color:#fff;font-weight:700;padding:4px 8px}
.hours td{border-bottom:1px solid #ddd;padding:5px 8px;text-align:center}
.hours td.t{text-align:left;font-weight:700}
.hours-note{left:60px;top:1102px;font-size:12px;color:var(--sub)}
.address{left:400px;top:948px;width:280px;font-size:11px;line-height:1.6;color:var(--sub)}
.tel{left:400px;top:990px;display:flex;align-items:center;gap:6px;font-size:28px;font-weight:900;color:var(--orange-deep);white-space:nowrap}
.search{left:400px;top:1044px;display:flex;border:2px solid var(--orange);font-size:12px}
.search span{padding:3px 10px}
.search .btn{background:var(--orange);color:#fff;font-weight:700}
.url{left:400px;top:1078px;font-size:14px;font-weight:700}
.map{left:700px;top:948px;width:120px;height:150px;background:linear-gradient(135deg,#eeeae4,#d9d3cb)}
.station{left:400px;top:1112px;font-size:11px;color:var(--sub)}
.bottom-bar{left:0;top:1190px;width:848px;height:10px;background:var(--orange)}
</style>
</head>
<body>

<div class="abs hero-photo" role="img" aria-label="歯科医院スタッフと診療台の写真"></div>
<div class="abs day-tag">6月4日は「くるみ健口デー」</div>
<svg class="abs wave" viewBox="0 0 848 70" preserveAspectRatio="none" aria-hidden="true">
  <path d="M0 35 C150 0 300 60 460 30 C600 5 720 35 848 15 L848 70 L0 70Z" fill="#fff"/>
  <path d="M0 35 C150 0 300 60 460 30 C600 5 720 35 848 15" fill="none" stroke="var(--orange)" stroke-width="6"/>
</svg>

<div class="abs headline-rule" style="top:300px"></div>
<h1 class="abs headline">定期予防で治療いらず!</h1>
<div class="abs headline-rule" style="top:370px"></div>

<h2 class="abs story-title">虫歯や歯周病が少ない国<br>スウェーデンの秘密</h2>
<p class="abs story-body">先進国スウェーデンでは、出産前のお母さんへの予防指導から始まり、生後から子どもの20歳までは定期的な予防処置、検診を受けることが義務付けられており、国民全体で90%以上がメインテナンスを続けています。虫歯になってから治療する費用は高額になり、痛い思いもしなければなりません。虫歯予防のために定期的な歯科検診を受けましょう。</p>
<p class="abs story-lead">3ヶ月に1回の定期検診が虫歯予防につながります。</p>

<div class="abs guide-tag">定期検診のご案内</div>
<div class="abs compare">
  <div class="abs compare-title">80歳時の歯数の比較</div>
  <div class="abs stat" style="left:14px;top:24px"><small>定期検診受診率</small><b>2</b>%</div>
  <div class="abs stat" style="left:14px;top:78px"><small>80歳時の歯数</small><b>9</b>本</div>
  <svg class="abs" style="left:112px;top:34px" width="62" height="42" viewBox="0 0 62 42" aria-hidden="true">
    <rect width="62" height="42" fill="#fff" stroke="#ccc"/><circle cx="31" cy="21" r="12" fill="var(--japan-red)"/>
  </svg>
  <div class="abs country" style="left:112px;top:82px;width:62px">日本</div>
  <svg class="abs" style="left:206px;top:34px" width="62" height="42" viewBox="0 0 62 42" aria-hidden="true">
    <rect width="62" height="42" fill="var(--sweden-blue)"/><rect x="18" width="9" height="42" fill="var(--sweden-yellow)"/><rect y="16" width="62" height="9" fill="var(--sweden-yellow)"/>
  </svg>
  <div class="abs country" style="left:200px;top:82px;width:74px">スウェーデン</div>
  <div class="abs stat sw" style="left:290px;top:24px"><small>定期検診受診率</small><b>91</b>%</div>
  <div class="abs stat sw" style="left:290px;top:78px"><small>80歳時の歯数</small><b>25</b>本</div>
</div>

<div class="abs doctor-info">
  <p>ことりデンタルクリニック</p>
  <p class="name">院長 森田 千尋</p>
  <p>みなさまの「笑顔」と「健康な歯」を守るお手伝いをいたします。</p>
</div>
<div class="abs doctor-photo" role="img" aria-label="院長のポートレート写真"></div>

<section class="abs features-band"></section>
<div class="abs photo" style="left:40px;top:688px;width:250px;height:115px" role="img" aria-label="完全個室の診療室の写真"></div>
<div class="abs" style="left:300px;top:688px;width:210px">
  <p class="feat-title">完全個室診療室</p>
  <p class="feat-text">他の患者様の目を気にせず、落ち着いて治療を受けていただける完全個室の診療室をご用意しています。</p>
</div>
<div class="abs" style="left:530px;top:688px;width:280px">
  <p class="feat-title">キッズコーナー完備</p>
  <p class="feat-text">お子様連れでも安心してご来院いただけるよう、院内にキッズコーナーをご用意しています。</p>
</div>
<div class="abs photo" style="left:530px;top:758px;width:280px;height:48px" role="img" aria-label="キッズコーナーの写真"></div>

<div class="abs photo" style="left:40px;top:816px;width:110px;height:104px" role="img" aria-label="小児歯科の写真"></div>
<div class="abs" style="left:158px;top:816px;width:120px">
  <p class="feat-title">小児歯科</p>
  <p class="feat-text">お子様の歯を虫歯から守る予防処置を行います。</p>
</div>
<div class="abs" style="left:290px;top:816px;width:124px">
  <p class="feat-title">院内フルフラット</p>
  <p class="feat-text">段差のない院内でベビーカーも安心です。</p>
</div>
<div class="abs photo" style="left:420px;top:816px;width:100px;height:104px" role="img" aria-label="院内の写真"></div>
<div class="abs" style="left:530px;top:816px;width:150px">
  <p class="feat-title">駐車場7台完備</p>
  <p class="feat-text">お車でのご来院も便利です。</p>
</div>
<div class="abs photo" style="left:690px;top:816px;width:120px;height:104px" role="img" aria-label="駐車場の写真"></div>

<div class="abs clinic-name"><span class="clinic-dot"></span>ことりデンタルクリニック</div>
<div class="abs clinic-en">Kotori Dental Clinic</div>
<table class="abs hours">
  <tr><th>診療時間</th><th>月</th><th>火</th><th>水</th><th>木</th><th>金</th><th>土</th><th>日・祝</th></tr>
  <tr><td class="t">9:00〜13:00</td><td>●</td><td>●</td><td>●</td><td>●</td><td>●</td><td>●</td><td>－</td></tr>
  <tr><td class="t">15:00〜19:00</td><td>●</td><td>●</td><td>●</td><td>●</td><td>●</td><td>●</td><td>－</td></tr>
</table>
<p class="abs hours-note">〜お盆・年末年始も通常診療〜</p>

<p class="abs address">〒000-0000 東京都みどり区あおば町3-12-5<br>休診日 日曜・祝日</p>
<div class="abs tel">
  <svg width="28" height="28" viewBox="0 0 24 24" aria-hidden="true"><path fill="var(--orange)" d="M6.6 10.8a15 15 0 0 0 6.6 6.6l2.2-2.2a1 1 0 0 1 1-.25 11.4 11.4 0 0 0 3.6.57 1 1 0 0 1 1 1V20a1 1 0 0 1-1 1A17 17 0 0 1 3 4a1 1 0 0 1 1-1h3.5a1 1 0 0 1 1 1c0 1.25.2 2.45.57 3.57a1 1 0 0 1-.25 1Z"/></svg>
  0120-000-482
</div>
<div class="abs search"><span>ことりデンタルクリニック</span><span class="btn">検索</span></div>
<p class="abs url">http://www.kotori-dc.example/</p>
<p class="abs station">■最寄り駅 さくら台駅 徒歩5分</p>
<div class="abs map" role="img" aria-label="医院周辺の地図"></div>
<div class="abs bottom-bar"></div>

</body>
</html>
```